Flyer to promote an IT Innovation Fest

BRN Grindstone Gala 2018

We are looking to implement a new Innovation program that uses the Marlow LaunchCrate concept. Team Members will receive a red box that contains a set of 20 flash cards that help them to bring an innovative idea to life (based on a business problem or friction point).
We are looking to create a cover page for our 'Red Box' via way of a 1 page flyer.
We want to call it the 'BRN Grindstone Gala 2018'. We would like the 1 page flyer to look super cool and also have some kind of cool cartoon imagery to bring it to life.
We also want to incorporate our logo into the page somewhere as well.

Ideally, we'd also like to get a logo called 'Grindstone Gala' that we could use on some of our collateral as well. I thought it might be best to create the 1 pager flyer first, then we could look to pull a Grindstone Gala logo off that. Please let me know though whether it would be easier to create the logo first, then create the flyer).

Skyward Ridge Systems are a support business to Skyward Ridge Journeys Group which is the largest travel retailer in Australia. Our IT area has around 150 permanent team members. We have a fun culture and can push the boundaries with our imagery as the flyer will be for internal distribution only.

I have attached the Marlow Flash cards that this 1 pager will be the cover page for.

Target Market(s)

Members of the Skyward Ridge Systems team (internal marketing)

Industry/Entity Type

It Company

Requirements
Must have
• Our BRN Logo
• A super cool, innovative, funky look (with some kind of cartoon imagery)
• We need to be able to edit the flyer to add some text
Nice to have
• Stay within the colour theme of the 'Start Here' page on the Marlow attachment

```html
<!DOCTYPE html>
<html lang="en">
<head>
<meta charset="utf-8">
<title>BRN Grindstone Gala 2018 – Flyer</title>
<link rel="stylesheet" href="https://fonts.googleapis.com/css2?family=Oswald:wght@600&display=swap">
<style>
  :root {
    --page-bg: #ffffff;
    --flyer-bg: #ffffff;
    --ink: #4a4a4a;
    --red-dark: #7a0208;
    --red-deep: #a3060c;
    --red-mid: #c8282c;
    --red-bright: #f06464;
    --red-soft: #f7bcbc;
  }
  html, body {
    margin: 0;
    width: 1200px;
    height: 1200px;
    overflow: hidden;
    background: var(--page-bg);
  }
  .flyer {
    position: absolute;
    left: 279px;
    top: 124px;
    width: 642px;
    height: 952px;
    background: var(--flyer-bg);
    overflow: hidden;
  }
  .flyer__art {
    position: absolute;
    left: 0;
    top: 0;
    width: 642px;
    height: 952px;
  }
  .flyer__title {
    position: absolute;
    left: 0;
    width: 100%;
    margin: 0;
    text-align: center;
    white-space: nowrap;
    font-family: "Oswald", "Arial Narrow", sans-serif;
    font-weight: 600;
    color: var(--ink);
    line-height: 1;
    letter-spacing: 0;
  }
  .flyer__code {
    top: 582px;
    font-size: 66px;
  }
  .flyer__name {
    top: 666px;
    font-size: 52px;
  }
</style>
</head>
<body>
  <main class="flyer">
    <svg class="flyer__art" viewBox="0 0 642 952" xmlns="http://www.w3.org/2000/svg">
      <defs>
        <linearGradient id="pattern-tone" x1="0" y1="0" x2="1" y2="1">
          <stop offset="0" stop-color="var(--red-bright)"/>
          <stop offset="0.18" stop-color="var(--red-mid)"/>
          <stop offset="0.32" stop-color="var(--red-soft)"/>
          <stop offset="0.46" stop-color="var(--red-deep)"/>
          <stop offset="0.6" stop-color="var(--red-bright)"/>
          <stop offset="0.74" stop-color="var(--red-dark)"/>
          <stop offset="0.88" stop-color="var(--red-mid)"/>
          <stop offset="1" stop-color="var(--red-bright)"/>
        </linearGradient>
        <linearGradient id="pattern-tone-low" x1="0" y1="0" x2="1" y2="1">
          <stop offset="0" stop-color="var(--red-soft)"/>
          <stop offset="0.25" stop-color="var(--red-deep)"/>
          <stop offset="0.5" stop-color="var(--red-bright)"/>
          <stop offset="0.75" stop-color="var(--red-mid)"/>
          <stop offset="1" stop-color="var(--red-soft)"/>
        </linearGradient>
      </defs>
      <polygon class="flyer__pattern flyer__pattern--top" role="img"
        aria-label="Geometric mosaic of red, crimson and pink triangles"
        fill="url(#pattern-tone)"
        points="0,0 642,0 642,524 581,558 523,524 463,558 405,524 347,558 288,524 229,558 170,524 111,558 52,524 0,552"/>
      <polygon class="flyer__pattern flyer__pattern--bottom" role="img"
        aria-label="Geometric mosaic of red, crimson and pink triangles"
        fill="url(#pattern-tone-low)"
        points="0,796 52,796 111,762 170,796 229,762 288,796 347,762 405,796 463,762 523,796 581,762 642,796 642,952 0,952"/>
    </svg>
    <h1 class="flyer__title flyer__code">BRN</h1>
    <p class="flyer__title flyer__name">BRN GRINDSTONE GALA 2018</p>
  </main>
</body>
</html>
```